wealth management firm, professional group, new model

we have a logo that works but we need a card, white background using our colors...clean look

our tag line if can be used in

The Bridge From Client to Owner

```html
<!DOCTYPE html>
<html lang="en">
<head>
<meta charset="utf-8">
<title>Arvelo Wealth Partners – Business Card</title>
<link rel="stylesheet" href="https://fonts.googleapis.com/css2?family=Montserrat:wght@400;500;700&display=swap">
<style>
  :root {
    --navy: #172d50;
    --white: #ffffff;
    --ink: #2b2f38;
    --backdrop: #d8d8d8;
  }
  * { box-sizing: border-box; margin: 0; padding: 0; }
  html, body { width: 1200px; height: 1018px; overflow: hidden; }
  body {
    background: var(--backdrop);
    font-family: "Montserrat", sans-serif;
    position: relative;
  }
  .card {
    position: absolute;
    width: 560px;
    height: 320px;
    box-shadow: 0 14px 30px rgba(0,0,0,0.22);
    overflow: hidden;
  }
  .card--front { left: 50px; top: 520px; background: var(--white); color: var(--navy); }
  .card--back  { left: 590px; top: 150px; background: var(--navy); color: var(--white); }

  .wordmark { text-align: center; }
  .wordmark__name {
    font-weight: 500;
    letter-spacing: 0.42em;
    padding-left: 0.42em;
    line-height: 1;
  }
  .wordmark__sub {
    font-weight: 500;
    letter-spacing: 0.22em;
    padding-left: 0.22em;
    line-height: 1;
  }

  .card--front .wordmark { padding-top: 34px; }
  .card--front .wordmark__name { font-size: 44px; }
  .card--front .wordmark__sub { font-size: 15px; margin-top: 8px; }

  .person { text-align: center; margin-top: 16px; }
  .person__name { font-size: 27px; font-weight: 700; letter-spacing: 0.01em; }
  .person__title { font-size: 15px; font-weight: 400; color: var(--ink); margin-top: 2px; }

  .contacts {
    position: absolute;
    left: 0; right: 0; bottom: 50px;
    display: flex;
    justify-content: center;
    gap: 14px;
    font-size: 12px;
    color: var(--ink);
  }
  .contact { display: flex; flex-direction: column; align-items: center; gap: 6px; }
  .contact svg { width: 12px; height: 12px; fill: var(--navy); }
  .contact__sep { align-self: flex-end; }

  .address-band {
    position: absolute;
    left: 0; right: 0; bottom: 0;
    height: 36px;
    background: var(--navy);
    color: var(--white);
    font-size: 13px;
    display: flex; align-items: center; justify-content: center;
    letter-spacing: 0.02em;
  }

  .card--back .wordmark {
    position: absolute; inset: 0;
    display: flex; flex-direction: column; align-items: center; justify-content: center;
  }
  .card--back .wordmark__name { font-size: 50px; }
  .card--back .wordmark__sub { font-size: 17px; margin-top: 10px; }
</style>
</head>
<body>

  <section class="card card--back" aria-label="Card back">
    <div class="wordmark">
      <div class="wordmark__name">ARVELO</div>
      <div class="wordmark__sub">WEALTH PARTNERS</div>
    </div>
  </section>

  <section class="card card--front" aria-label="Card front">
    <div class="wordmark">
      <div class="wordmark__name">ARVELO</div>
      <div class="wordmark__sub">WEALTH PARTNERS</div>
    </div>

    <div class="person">
      <div class="person__name">MARTEN VALE</div>
      <div class="person__title">General Manager</div>
    </div>

    <div class="contacts">
      <div class="contact">
        <svg viewBox="0 0 16 16" aria-hidden="true"><path d="M1 3h14v10H1z M1 3l7 6 7-6" fill="var(--navy)"/><path d="M1.5 3.5l6.5 5.5 6.5-5.5" stroke="#fff" stroke-width="1.2" fill="none"/></svg>
        <span>info@arvelowealth.com</span>
      </div>
      <span class="contact__sep">|</span>
      <div class="contact">
        <svg viewBox="0 0 16 16" aria-hidden="true"><path d="M4 1l2.5 3-1.5 2c1 2 3 4 5 5l2-1.5 3 2.5-1.5 2.5C7 16 0 9 1.5 2.5z"/></svg>
        <span>(555) 014-2290</span>
      </div>
      <span class="contact__sep">|</span>
      <div class="contact">
        <svg viewBox="0 0 16 16" aria-hidden="true"><circle cx="8" cy="8" r="7"/><path d="M1 8h14M8 1c3 3 3 11 0 14M8 1c-3 3-3 11 0 14" stroke="#fff" stroke-width="1" fill="none"/></svg>
        <span>www.arvelowealth.com</span>
      </div>
    </div>

    <div class="address-band">42 Linden Court, Suite 200, Fairview, TN 38000</div>
  </section>

</body>
</html>
```